Maplewood Surgery Brochure Design

Maplewood Surgery (maplewoodsurgery.example)

Is a comprehensive breast care center that focuses on caring for women with breast cancer and other breast pathologies. We need a promotional and marketing brochure, in a tri-fold format, to provide information about our office and describe the services that we offer.

Deliverable

* The brochure should be completed by August 24th
* We will need the necessary files to get the brochure printed (.ai, .indd, etc).

Target Market(s)

Primarily patients of age between 30+ and 70+. The brochure will also be placed in doctor's waiting room

Industry/Entity Type

Marketing

Requirements
Must have
• * Make use of the color scheme as the website (http://maplewoodsurgery.example, http://maplewoodsurgery.example/static/theme-fuchsia.png)
* Incorporate the following graphic elements:
* The company’s logo (provided as an attachment)
* At least one images from the homepage
* Photos of the primary doctor and her staff
* Map to show the office location and phone number
* Enclose a breast cancer self-exam card (http://maplewoodsurgery.example/static/shower-card.jpg)
* A portion of the brochure must be detachable and serve as business cards that can be cut off (see attachment).
Nice to have
• Here is an example of a brochure that we like:

http://designbazaro.example/item/flexible-trifold-brochure/318274?WT.ac=search_item&WT.seg_1=search_item&WT.z_author=mendavik

```html
<!DOCTYPE html>
<html lang="en">
<head>
<meta charset="utf-8">
<title>Maplewood Surgery – Tri-fold Brochure Interior</title>
<link href="https://fonts.googleapis.com/css2?family=EB+Garamond:wght@400;500&display=swap" rel="stylesheet">
<style>
  :root {
    --stage: #8c8c8c;
    --stage-light: #c4c4c4;
    --magenta-deep: #7a0f3a;
    --magenta: #a51e58;
    --magenta-bright: #c43472;
    --pink-soft: #f3cfe0;
    --pink-pale: #fbeef4;
    --blush: #e9a3c4;
    --paper: #ffffff;
    --ink: #231f20;
    --frame: #d87aa8;
  }
  * { box-sizing: border-box; margin: 0; padding: 0; }
  html, body { width: 1200px; height: 900px; overflow: hidden; }
  body {
    position: relative;
    background: radial-gradient(ellipse at center, var(--stage-light) 0%, var(--stage) 100%);
    font-family: "EB Garamond", Garamond, serif;
    color: var(--ink);
  }
  .brochure {
    position: absolute; left: 18px; top: 38px; width: 1164px; height: 817px;
    background: linear-gradient(180deg, var(--magenta-deep) 0%, var(--magenta) 45%, var(--magenta-bright) 75%, var(--blush) 100%);
    overflow: hidden;
  }
  .fold-band {
    position: absolute; top: 0; bottom: 0; width: 34px;
    background: linear-gradient(90deg, rgba(255,255,255,0.05), rgba(255,255,255,0.22), rgba(255,255,255,0.05));
  }
  .fold-band.first { left: 370px; }
  .fold-band.second { left: 758px; }
  .top-rule {
    position: absolute; left: 0; right: 0; top: 8px; height: 26px;
    background: rgba(255,255,255,0.12);
  }
  .bottom-sweep { position: absolute; left: 0; bottom: 0; width: 1164px; height: 260px; }
  .bloom { position: absolute; border-radius: 50%; }
  .bloom.left-top { left: 200px; top: 40px; width: 200px; height: 220px;
    background: radial-gradient(circle, rgba(255,255,255,0.9), rgba(255,255,255,0)); }
  .bloom.left-bottom { left: -20px; top: 665px; width: 150px; height: 150px;
    background: radial-gradient(circle, #f5d36a 0%, #e76f9c 35%, rgba(240,180,205,0.9) 60%, rgba(255,255,255,0) 72%); }
  .bloom.middle { left: 410px; top: 600px; width: 260px; height: 220px;
    background: radial-gradient(circle, #f7e0a0 0%, #f4c6d9 30%, rgba(250,225,236,0.85) 55%, rgba(255,255,255,0) 72%); }
  .bloom.middle-small { left: 675px; top: 740px; width: 90px; height: 80px;
    background: radial-gradient(circle, #f5d36a 0%, #f3bcd3 40%, rgba(255,255,255,0) 72%); }
  .bloom.corner { left: 1100px; top: -4px; width: 64px; height: 60px;
    background: radial-gradient(circle, #f5d36a 0%, #f3bcd3 40%, rgba(255,255,255,0) 72%); }
  .text-panel {
    position: absolute; background: var(--paper);
    font-size: 15px; line-height: 18.6px;
  }
  .text-panel p { margin: 0; }
  .panel-about { left: 24px; top: 42px; width: 341px; height: 520px; border-radius: 0 28px 0 0; padding: 16px 20px 0 26px; }
  .panel-care { left: 410px; top: 42px; width: 342px; height: 662px; padding: 16px 20px 0 27px; }
  .panel-doctor { left: 794px; top: 42px; width: 348px; height: 575px; border-radius: 28px 0 0 0; padding: 16px 20px 0 26px; }
  .doctor-portrait {
    float: right; width: 108px; height: 134px; margin: -10px -38px 4px 8px;
    background: linear-gradient(160deg, #6a6a6a, #2e2a2a);
    border: 2px solid #ddd;
  }
  .team-photo {
    position: absolute; left: 40px; top: 555px; width: 310px; height: 205px;
    transform: rotate(-9deg);
    border: 9px solid var(--frame); border-radius: 14px;
    background: linear-gradient(160deg, #b7b1ab, #5a5048);
    box-shadow: 0 4px 10px rgba(0,0,0,0.25);
  }
  .contact-block {
    position: absolute; left: 776px; top: 603px; width: 390px; height: 220px;
    border-radius: 40px 0 0 0;
    background: linear-gradient(180deg, var(--magenta) 0%, var(--magenta-bright) 60%, var(--blush) 100%);
  }
  .brand-name {
    position: absolute; right: 12px; bottom: 12px;
    font-family: "EB Garamond", Garamond, serif; font-size: 22px; color: var(--pink-pale);
  }
</style>
</head>
<body>
  <section class="brochure">
    <div class="top-rule"></div>
    <div class="fold-band first"></div>
    <div class="fold-band second"></div>

    <svg class="bottom-sweep" viewBox="0 0 1164 260" aria-hidden="true">
      <defs>
        <linearGradient id="sweepFill" x1="0" y1="0" x2="0" y2="1">
          <stop offset="0" stop-color="#ffffff"/>
          <stop offset="1" stop-color="#f1bcd3"/>
        </linearGradient>
      </defs>
      <path d="M0 0 C300 60 560 120 780 150 L780 260 L0 260 Z" fill="url(#sweepFill)"/>
    </svg>

    <div class="bloom left-top" role="img" aria-label="Soft white lotus flower decoration"></div>
    <div class="bloom middle" role="img" aria-label="Pale pink lotus flower decoration"></div>
    <div class="bloom middle-small" role="img" aria-label="Small pink lotus flower"></div>
    <div class="bloom corner" role="img" aria-label="Small pink lotus flower"></div>

    <article class="text-panel panel-about">
      <p>We provide a caring, intimate environment where your dignity and health come first.Conveniently, we are situated next to Linden Hospital, in the Harrow Whitfield Cancer Center. This means that any necessary diagnostic and treatment modalities are at our fingertips.</p>
      <p>We understand the anxiety involved with breast problems. We know that when you are told that you need to be evaluated more closely, you want answers as quickly as possible. We are hereto help you, striving to be as proficient as possible. Being dedicated to breast care, we have a wealth of up-to-date knowledge about current breast care concepts. Your doctor will listen to your concerns and work with you to make sure you understand your options.</p>
      <p>Our knowledgeable staff will help to alleviate your anxiety with timely appointments, education and compassion. We will make sure you have all the facts to make the best decisions about your health care.</p>
    </article>

    <div class="team-photo" role="img" aria-label="Photo of the doctor and a staff member standing together"></div>
    <div class="bloom left-bottom" role="img" aria-label="Pink lotus flower decoration"></div>

    <article class="text-panel panel-care">
      <p>Dedicated -- to bringing to you the most fresh and knowledgeable breast care, including all diagnostic studies and any surgical techniques necessary.</p>
      <p>Unified team approach -- one that includes communication with your primary doctor, laboratory, radiology and ancillary services in a coordinated effort. Appropriate resources -- including support groups, therapy, oncology, radiation oncology, cancer societies and more.</p>
      <p>Experience: Dr. Kowalczyk has focused her entire practice on breast surgery, as she feels thatthis is the field in which she excels. Being fellowship-trained in Oncoplastic Breast Surgery, sheintensely believes in comprehensive breast care and being with the patient through the entire experience. She is comfortable treating patients of all ages, from birth to the elderly. Being compassionate and caring, she strives to project these qualities into everything that she puts her hands on. Dr. Kowalczyk is passionate about making sure that her patients get the best care,that they are well-informed, and treated with the dignity and respect that they deserve.</p>
    </article>

    <div class="contact-block">
      <span class="brand-name">Maplewood Surgery</span>
    </div>

    <article class="text-panel panel-doctor">
      <div class="doctor-portrait" role="img" aria-label="Portrait photo of Dr. Maren Kowalczyk"></div>
      <p>Dr. Maren Kowalczyk is the first fellowship-trained breast surgeon south of Ashford, Ill., and is excited to come home and bring her expertise to the women of Southern Illinois.</p>
      <p>She deeply understands that you need to heal physically... emotionally... spiritually. This is truly comprehensive breast care.</p>
      <p>Services include:</p>
      <p>Breast pain and other nonsurgical management of breast problems Treatment of diseases of the breast (abscesses, gynecomastia) Biopsies (including minimally invasive with ultrasound or stereotactic guidance) Cryoablation (freezing) of certain breast conditions Breast resections (as needed for benign or malignant disease processes) Lymph node resections (including sentinel lymph node excisions) Breast reconstruction and balancing of the “other” breast as needed Breast reductions (for cancer or for burdensome breasts) Mastopexies (breast lifts for cancer or droopy breasts) Of course, this is not an exhaustive list. If there is a procedure you are interested in, please call our office to find out if we offer it.</p>
    </article>
  </section>
</body>
</html>
```